Business Card Design

We are a trucking company that do a lot of business one on one with shippers. Our enthusiasm, honesty and hard work make us a great company to work with. We want to not only leave a lasting impression by the professionalism of our drivers but also give them something to remember us by for the future. I have a logo already designed that matches the same logo on the trucks. Its simple yet captures people to remember the name. We are expanding our coverage area by almost 700 miles and want to get our brand out there by having shippers call us to come back and conduct more business. I would like part of the logo itself raised but the shadowing not to give it a unique look and feel.
Industry/Entity Type
Trucking Company
Contact Information for Business Card
K&M Hauling LLC
Kurt & Melissa Haverford
308.555.0142 Kurt
308.555.0187 Melissa
kmhaulingllc@examplemail.net
Look and feel

```html
<!DOCTYPE html>
<html lang="en">
<head>
<meta charset="utf-8">
<title>K&amp;M Hauling LLC – Business Card</title>
<link rel="stylesheet" href="https://fonts.googleapis.com/css2?family=Oleo+Script:wght@700&family=Arimo:wght@400&display=swap">
<style>
  :root {
    --backdrop: #a4a4a4;
    --band-dark: #242424;
    --band-light: #ffffff;
    --band-mid: #6f6f6f;
    --rule: #3a3a3a;
    --ink-light: #ffffff;
    --ink-dark: #1e1e1e;
  }
  html, body {
    margin: 0;
    padding: 0;
    width: 1200px;
    height: 1200px;
    overflow: hidden;
    background: var(--backdrop);
  }
  .canvas {
    width: 1200px;
    height: 1200px;
    display: flex;
    align-items: center;
    justify-content: center;
  }
  .business-card {
    width: 900px;
    height: 514px;
    display: flex;
    flex-direction: column;
    background: var(--band-light);
    box-shadow: 0 6px 18px rgba(0,0,0,0.25);
  }
  .name-band {
    height: 148px;
    background: var(--band-dark);
    color: var(--ink-light);
    display: flex;
    flex-direction: column;
    align-items: center;
    justify-content: center;
    font-family: "Oleo Script", cursive;
    font-weight: 700;
    font-size: 40px;
    line-height: 1.2;
    text-align: center;
  }
  .brand-band {
    flex: 1;
    position: relative;
    display: flex;
    align-items: center;
    justify-content: center;
    border-top: 3px solid var(--band-light);
    border-bottom: 3px solid var(--band-light);
    box-shadow: inset 0 3px 0 var(--rule), inset 0 -3px 0 var(--rule);
    padding-top: 6px;
  }
  .brand-band::before,
  .brand-band::after {
    content: "";
    position: absolute;
    left: 0;
    right: 0;
    height: 2px;
    background: var(--rule);
  }
  .brand-band::before { top: 10px; }
  .brand-band::after { bottom: 10px; }
  .brand-name {
    font-family: "Arimo", Arial, sans-serif;
    font-weight: 400;
    font-size: 46px;
    color: var(--ink-dark);
  }
  .contact-band {
    height: 145px;
    background: var(--band-mid);
    color: var(--ink-light);
    font-family: "Arimo", Arial, sans-serif;
    font-size: 25px;
    line-height: 34px;
    padding: 20px 0 0 58px;
    box-sizing: border-box;
  }
  .contact-line {
    display: flex;
    align-items: center;
    gap: 10px;
  }
  .contact-icon {
    width: 18px;
    height: 20px;
    flex: none;
  }
</style>
</head>
<body>
<main class="canvas">
  <section class="business-card">
    <header class="name-band">
      <span>Kurt &amp;</span>
      <span>Melissa Haverford</span>
    </header>
    <div class="brand-band">
      <span class="brand-name">K&amp;M Hauling LLC</span>
    </div>
    <footer class="contact-band">
      <div class="contact-line">
        <svg class="contact-icon" viewBox="0 0 18 20" aria-hidden="true">
          <rect x="4" y="1" width="10" height="18" rx="2" fill="none" stroke="#fff" stroke-width="2"/>
          <line x1="7" y1="15" x2="11" y2="15" stroke="#fff" stroke-width="2"/>
        </svg>
        <span>308.555.0142 (Kurt)</span>
      </div>
      <div class="contact-line">
        <svg class="contact-icon" viewBox="0 0 18 20" aria-hidden="true">
          <rect x="4" y="1" width="10" height="18" rx="2" fill="none" stroke="#fff" stroke-width="2"/>
          <line x1="7" y1="15" x2="11" y2="15" stroke="#fff" stroke-width="2"/>
        </svg>
        <span>308.555.0187 (Melissa)</span>
      </div>
      <div class="contact-line">
        <svg class="contact-icon" viewBox="0 0 18 20" aria-hidden="true">
          <rect x="1" y="5" width="16" height="12" fill="none" stroke="#fff" stroke-width="2"/>
          <polyline points="1,5 9,12 17,5" fill="none" stroke="#fff" stroke-width="2"/>
        </svg>
        <span>kmhaulingllc@examplemail.net</span>
      </div>
    </footer>
  </section>
</main>
</body>
</html>
```